all sorted property services

Target Market(s)

General letter head for emails and letter quotes ect

Colors
0054AA
0677BA
7BADD7
CADEEF
E8F1F8
0094D4
00A9DD
6FCCEA
C7EBF8
E9F6FB

Requirements
Must have
• logo phone email website names
Nice to have
• what we do (from the website)

```html
<!DOCTYPE html>
<html lang="en">
<head>
<meta charset="utf-8">
<title>All Sorted Property Services – Letterhead</title>
<link rel="stylesheet" href="https://fonts.googleapis.com/css2?family=Arimo:wght@400;700&family=Open+Sans:wght@400&display=swap">
<style>
:root{
  --page:#f6f5f5;
  --ink:#3d3d3d;
  --ink-soft:#4a4a4a;
  --brand-deep:#0054AA;
  --brand-mid:#0677BA;
  --brand-bright:#0094D4;
  --navy:#262a74;
  --rule-grey:#8f8f8b;
}
*{margin:0;padding:0;box-sizing:border-box}
html,body{width:942px;height:1200px;overflow:hidden;background:var(--page)}
.letterhead{position:relative;width:942px;height:1200px;background:var(--page);font-family:"Arimo",Arial,sans-serif;color:var(--ink)}
.brand{position:absolute;left:64px;top:122px;display:flex;align-items:center;gap:10px}
.brand-dot{width:22px;height:22px;border-radius:50%;background:var(--brand-mid)}
.brand-name{font-weight:700;font-size:19px;letter-spacing:.5px;color:var(--brand-deep);line-height:1.15;text-transform:uppercase}
.contact{position:absolute;left:634px;top:66px;font-family:"Open Sans",Arial,sans-serif;font-style:normal;font-size:14px;line-height:18px;color:#222;text-transform:uppercase}
.contact-line{display:flex;align-items:center;gap:8px;text-transform:none;margin-top:4px}
.contact-line:first-of-type{margin-top:6px}
.contact-line svg{width:13px;height:13px;fill:var(--brand-deep)}
.salutation{position:absolute;left:64px;top:280px;font-size:26px;color:var(--ink-soft)}
.body-copy{position:absolute;left:64px;width:812px;font-size:14px;line-height:15.6px;text-align:justify;color:var(--ink-soft);hyphens:auto}
.p1{top:366px}.p2{top:472px}.p3{top:573px}.p4{top:697px}
.closing{position:absolute;left:64px;top:793px;font-size:14px;color:var(--ink-soft)}
.signature{position:absolute;left:74px;top:876px;width:124px;height:42px;background:linear-gradient(90deg,#dedee4,#ececef);border-radius:4px}
.signer{position:absolute;left:76px;top:941px;font-size:18px;color:var(--ink-soft)}
.signer-role{position:absolute;left:76px;top:967px;font-size:14px;color:var(--ink-soft)}
.footer-rule{position:absolute;left:0;top:1112px;width:942px;height:6px;background:var(--rule-grey)}
.footer{position:absolute;left:0;bottom:0;width:942px;height:76px;background:linear-gradient(90deg,var(--navy),var(--brand-bright) 50%,var(--navy));display:flex;align-items:flex-end;justify-content:center;padding-bottom:8px}
.footer-url{font-family:"Open Sans",Arial,sans-serif;font-size:14px;color:#fff}
</style>
</head>
<body>
<main class="letterhead">
  <header>
    <div class="brand">
      <span class="brand-dot"></span>
      <span class="brand-name">All Sorted<br>Property Services</span>
    </div>
    <address class="contact">
      14 Kestrel Avenue<br>
      Palm Cove Heights, Queensland<br>
      4221 Australia
      <div class="contact-line">
        <svg viewBox="0 0 24 24"><path d="M6.6 10.8a15.2 15.2 0 0 0 6.6 6.6l2.2-2.2a1 1 0 0 1 1-.25 11.4 11.4 0 0 0 3.6.57 1 1 0 0 1 1 1V20a1 1 0 0 1-1 1A17 17 0 0 1 3 4a1 1 0 0 1 1-1h3.5a1 1 0 0 1 1 1c0 1.25.2 2.45.57 3.57a1 1 0 0 1-.25 1z"/></svg>
        954-555-0142
      </div>
      <div class="contact-line">
        <svg viewBox="0 0 24 24"><path d="M2 5h20v14H2z"/><path d="M3 6l9 7 9-7" stroke="#fff" stroke-width="1.6" fill="none"/></svg>
        info@allsortedservices.com.au
      </div>
    </address>
  </header>

  <p class="salutation">Dear Mr. Carter,</p>

  <p class="body-copy p1">Lorem ipsum dolor sit amet, consectetur adipiscing elit. Donec orci purus, luctus vitae dignissim eu, iaculis sed purus. Vivamus faucibus, ipsum nec aliquet viverra, leo mauris condimentum ligula, sit amet sagittis enim ligula quis arcu. Nam egestas tortor id nisi porttitor mattis. In tortor ante, ultricies in suscipit a, tempus non massa. Vivamus et auctor mi. Fusce vel massa nulla. Phasellus nec eros mauris, et scelerisque orci.</p>
  <p class="body-copy p2">Donec malesuada orci vitae nulla accumsan porta a id massa. Quisque accumsan iaculis magna sit amet fringilla. Maecenas consequat, magna eget tincidunt semper, odio nibh rutrum mi, id feugiat ante nisi eu risus. Vestibulum nunc orci, rhoncus a placerat in, ultricies in mi. Cras mattis varius eros, vel fringilla nisi suscipit eget. Quisque scelerisque sagittis nulla at porttitor.</p>
  <p class="body-copy p3">Sed id augue vitae urna euismod commodo aliquet a quam. Pellentesque arcu velit, cursus et malesuada ut, consequat et diam. Nullam erat sem, rhoncus id ullamcorper vitae, rhoncus et arcu. In ultricies ultricies nulla, ut rutrum nisi iaculis at. Donec eu magna a metus ornare faucibus. Fusce aliquet faucibus ultricies. Morbi semper, est id tincidunt gravida, sem arcu adipiscing lacus, ac bibendum nulla leo eu purus. Quisque nec diam sed risus consectetur a ccumsan quis quis nibh. Vestibulum id purus lorem.</p>
  <p class="body-copy p4">It is a long established fact that a reader will be distracted by the readable content of a page when looking at its layout. The point of using Lorem Ipsum is that it has a more-or-less normal distribution of letters, as opposed to using 'Content here, content here', making it look like readable English. Many desktop publishing packages</p>

  <p class="closing">Sincerely,</p>
  <div class="signature" role="img" aria-label="Handwritten signature"></div>
  <p class="signer">James Carter</p>
  <p class="signer-role">CEO/ Founder</p>

  <div class="footer-rule"></div>
  <footer class="footer">
    <p class="footer-url">www.allsortedservices.com.au</p>
  </footer>
</main>
</body>
</html>
```